Flyer Promo

Looking for a flyer design (3.75" x8.25") to launch our new Internet Service Provider business. I will upload a file of what should be on the double-sided flyer and our company logo and icons. Looking for a minimalist eye catching design.

Colors

```html
<!DOCTYPE html>
<html lang="en">
<head>
<meta charset="utf-8">
<title>Fieldline Net – Flyer</title>
<link href="https://fonts.googleapis.com/css2?family=Oswald:wght@700&family=Roboto:wght@400;500;700&display=swap" rel="stylesheet">
<style>
  :root{
    --blue:#1479d6;
    --blue-dark:#0b5fb3;
    --ink:#1f1f1f;
    --text:#333;
    --grey-bg:#d9d9d9;
    --paper:#f4f5f6;
    --table-bg:#e4f1fb;
    --navy:#1d2240;
    --red:#e3262b;
  }
  *{box-sizing:border-box;margin:0;padding:0}
  html,body{width:786px;height:1200px;overflow:hidden}
  body{background:var(--grey-bg);font-family:"Roboto",Arial,sans-serif;color:var(--text);position:relative}
  .flyer{position:absolute;top:215px;width:350px;height:770px;background:var(--paper);box-shadow:0 8px 22px rgba(0,0,0,.25);overflow:hidden}
  .flyer--front{left:28px}
  .flyer--back{left:408px}
  .abs{position:absolute}
  .center{left:0;right:0;text-align:center}

  .brand{position:absolute;left:0;right:0;display:flex;align-items:center;justify-content:center;gap:8px}
  .brand__dot{width:30px;height:30px;border-radius:50%;background:var(--blue)}
  .brand__name{font-family:"Roboto",Arial,sans-serif;font-weight:700;font-size:26px;color:var(--blue)}

  .front-header{position:absolute;left:0;top:0;width:350px;height:240px;background:linear-gradient(180deg,#f7f7f8,#e3e5e8)}
  .headline{font-family:"Oswald",Impact,sans-serif;font-weight:700;line-height:1;letter-spacing:-.5px}
  .headline--internet{top:70px;font-size:64px;color:var(--ink)}
  .headline--service{top:134px;font-size:58px;color:var(--blue)}
  .headline--sub{top:198px;font-family:"Roboto",Arial,sans-serif;font-weight:700;font-size:22px;color:var(--ink)}
  .section-title{top:252px;font-size:21px;font-weight:500;color:var(--blue)}

  .bullet{position:absolute;font-size:7.6px;line-height:1.25;color:#444;padding-left:14px}
  .bullet::before{content:"";position:absolute;left:0;top:1px;width:8px;height:8px;border-radius:50%;background:var(--blue)}
  .bullet--justify{text-align:justify}

  .badge{position:absolute;left:200px;top:322px;width:130px;height:84px}
  .badge__time{position:absolute;left:10px;top:0;font-family:"Oswald",sans-serif;font-weight:700;font-size:22px;color:var(--red);display:flex;align-items:center;gap:4px}
  .badge__clock{width:20px;height:20px;border:2px solid var(--red);border-radius:50%}
  .badge__shape{position:absolute;left:0;top:28px}
  .badge__for{position:absolute;left:14px;top:36px;font-size:5px;color:#fff}
  .badge__main{position:absolute;left:14px;top:41px;font-size:13px;color:#fff;letter-spacing:.3px}
  .badge__note{position:absolute;left:12px;top:60px;background:var(--red);color:#fff;font-size:5.4px;line-height:1.1;padding:1px 4px;border-radius:2px}

  .plans{position:absolute;left:26px;top:474px;width:298px;background:var(--table-bg);border:1px solid #cfe1f0}
  .plans__head{display:flex;height:18px}
  .plans__tab{flex:1;position:relative}
  .plans__tab span{position:absolute;left:14px;right:14px;top:0;height:15px;background:var(--blue);color:#fff;font-size:8px;font-weight:700;text-align:center;line-height:15px;clip-path:polygon(0 0,100% 0,92% 100%,8% 100%)}
  .plans__row{display:flex;height:23px;border-top:1px solid #fff}
  .plans__name{width:158px;padding:2px 6px 0 16px;font-size:6.4px;line-height:1.2;color:#555;border-right:1px solid #fff;display:flex;align-items:center}
  .plans__price{flex:1;text-align:center;font-size:8.5px;color:#333;display:flex;align-items:center;justify-content:center}
  .plans__price b{font-family:"Oswald",sans-serif;font-size:8.5px}
  .plans__price sup{font-size:5px}

  .footnote{position:absolute;left:26px;top:708px;width:160px;font-size:5.3px;line-height:1.35;color:#444}
  .contact{position:absolute;left:184px;top:706px;width:150px}
  .contact__name{font-size:9.5px;font-weight:500;color:var(--blue);margin-bottom:4px}
  .contact__line{display:flex;align-items:center;gap:6px;font-size:5.4px;color:#333;margin-bottom:4px}
  .contact__line svg{flex:none}

  .blue-band{position:absolute;left:0;bottom:0}

  .pitch{top:108px;font-size:15.5px;font-weight:500;line-height:1.23;color:var(--ink)}
  .join{top:228px;font-size:28px;font-weight:700;color:var(--blue)}
  .icon-circle{position:absolute;left:155px;width:40px;height:40px}
  .contact-big{font-size:15.5px;font-weight:500;color:var(--ink)}
  .call{top:440px;font-size:14px;font-weight:500;color:var(--blue);letter-spacing:.5px}
  .phone{top:458px;font-size:25px;font-weight:700;color:var(--ink);letter-spacing:.5px}
  .for-service{top:492px;font-size:16px;font-weight:500;color:var(--blue)}
  .proof{top:526px;font-size:15px;font-weight:500;line-height:1.28;color:var(--ink)}
  .proof small{display:block;font-size:12px;font-weight:400}
  .speed-result{position:absolute;left:40px;top:606px;width:270px;height:130px;border-radius:6px;background:linear-gradient(180deg,#24294a,var(--navy));box-shadow:0 2px 6px rgba(0,0,0,.3)}
</style>
</head>
<body>

<section class="flyer flyer--front">
  <div class="front-header"></div>

  <div class="brand" style="top:24px">
    <span class="brand__dot"></span>
    <span class="brand__name">Fieldline Net</span>
  </div>

  <div class="abs center headline headline--internet">INTERNET</div>
  <div class="abs center headline headline--service">SERVICE</div>
  <div class="abs center headline headline--sub">PROVIDER BUSINESS</div>

  <svg class="abs" style="left:0;top:190px" width="350" height="60" viewBox="0 0 350 60">
    <path d="M296 6 C340 10 342 46 300 52" fill="none" stroke="var(--blue)" stroke-width="3" stroke-dasharray="14 6"/>
    <line x1="18" y1="52" x2="300" y2="52" stroke="var(--blue)" stroke-width="4" stroke-dasharray="20 10"/>
  </svg>

  <div class="abs center section-title">Who We Are</div>
  <svg class="abs" style="left:105px;top:280px" width="140" height="4"><line x1="0" y1="2" x2="140" y2="2" stroke="var(--blue)" stroke-width="2" stroke-dasharray="14 4"/></svg>

  <p class="bullet bullet--justify" style="left:22px;top:298px;width:150px">Fieldline Net is a local, Millbrook based, Internet Service Provider. We use Canadian designed and manufactured equipment as much as possible and we are a licensed Service Provider with the national telecom regulator.</p>
  <p class="bullet" style="left:192px;top:298px;width:130px">Local service and support is available</p>

  <div class="badge">
    <div class="badge__time"><span class="badge__clock"></span>24/7</div>
    <svg class="badge__shape" width="130" height="50" viewBox="0 0 130 50">
      <path d="M4 0 H102 L128 25 L102 50 H4 Z" fill="var(--navy)" stroke="#c8ccd4" stroke-width="2"/>
    </svg>
    <span class="badge__for">FOR</span>
    <span class="badge__main">EMERGENCIES</span>
    <span class="badge__note">Free technical support<br>during business hours.</span>
  </div>

  <p class="bullet bullet--justify" style="left:22px;top:388px;width:150px">We have no term contracts or cancellation fees and your satisfaction is guaranteed or cancel at no cost.</p>
  <p class="bullet" style="left:22px;top:434px;width:306px">Full Plan speeds that are offered will be available at most all times. We upgrade our network capacity on a constant basis. Pings as low as 9 milliseconds and a network uptime of over 99 percent.</p>

  <div class="plans">
    <div class="plans__head">
      <div class="plans__tab" style="flex:0 0 158px"><span>Our Internet Plans</span></div>
      <div class="plans__tab"><span>NO DATA CAPS</span></div>
    </div>
    <div class="plans__row"><div class="plans__name">Plan 3 (3 Mbps Down and 1 Mbps Up)</div><div class="plans__price"><sup>$</sup><b>39.99</b>/month</div></div>
    <div class="plans__row"><div class="plans__name">Plan 5 (5 Mbps Down and 2 Mbps Up)</div><div class="plans__price"><sup>$</sup><b>54.99</b>/month</div></div>
    <div class="plans__row"><div class="plans__name">Plan 10 (10 Mbps Down and 3 Mbps Up)</div><div class="plans__price"><sup>$</sup><b>74.99</b>/month</div></div>
    <div class="plans__row"><div class="plans__name">Plan 18 (18 Mbps Down and 3 Mbps Up)</div><div class="plans__price"><sup>$</sup><b>99.99</b>/month</div></div>
    <div class="plans__row"><div class="plans__name">Plan 25 (25 Mbps Down and 4 Mbps Up)</div><div class="plans__price"><sup>$</sup><b>114.99</b>/month</div></div>
    <div class="plans__row"><div class="plans__name">Plan 50 (50 Mbps Down and 10 Mbps Up)*</div><div class="plans__price"><sup>$</sup><b>199.99</b>/month</div></div>
    <div class="plans__row" style="height:18px"><div class="plans__name">Static Public I.P. Address, IPv4</div><div class="plans__price"><sup>$</sup><b>15.00</b>/month</div></div>
    <div class="plans__row" style="height:18px"><div class="plans__name">Basic Installation of Service</div><div class="plans__price">No Charge</div></div>
    <div class="plans__row"><div class="plans__name">Residential towers supplied &amp; installed</div><div class="plans__price"><sup>$</sup><b>10</b>/foot typical</div></div>
  </div>

  <p class="footnote">* Full Speed Not Guaranteed during 8 PM to 10 PM peak times &amp; Not available at all tower sites (Plan 50 Only)<br><br>Billing available by Direct Debit or Credit Card.<br>Client Speeds verified by using TowerGauge.net</p>

  <div class="contact">
    <div class="contact__name">Fieldline Net</div>
    <div class="contact__line"><svg width="7" height="8" viewBox="0 0 7 8"><path d="M3.5 0a3 3 0 0 1 3 3c0 2-3 5-3 5S.5 5 .5 3a3 3 0 0 1 3-3z" fill="var(--blue)"/></svg>412 Cedar Hollow Road, Millbrook, ON K0A 1B2</div>
    <div class="contact__line"><svg width="7" height="6" viewBox="0 0 7 6"><rect width="7" height="6" fill="var(--ink)"/></svg>Sales@FieldlineNet.ca</div>
    <div class="contact__line"><svg width="7" height="7" viewBox="0 0 7 7"><circle cx="3.5" cy="3.5" r="3.5" fill="var(--blue)"/></svg>www.TowerGauge.net</div>
  </div>

  <svg class="blue-band" width="350" height="10" viewBox="0 0 350 10">
    <path d="M0 4 H250 L262 10 H0 Z" fill="var(--blue)"/>
    <path d="M262 10 L250 4 H350 V10 Z" fill="var(--blue-dark)" opacity=".3"/>
  </svg>
</section>

<section class="flyer flyer--back">
  <div class="brand" style="top:38px">
    <span class="brand__dot"></span>
    <span class="brand__name">Fieldline Net</span>
  </div>

  <p class="abs center pitch">While most Internet Service<br>Providers are busy Raising Prices,<br>we are busy Upgrading our Network<br>Performance.<br>(And not Raising Prices)</p>

  <div class="abs center join">Join Us At</div>
  <svg class="abs" style="left:88px;top:266px" width="175" height="4"><line x1="0" y1="2" x2="175" y2="2" stroke="var(--blue)" stroke-width="2" stroke-dasharray="22 4"/></svg>

  <svg class="icon-circle" style="top:286px" viewBox="0 0 40 40">
    <circle cx="20" cy="20" r="18" fill="#fff" stroke="var(--blue)" stroke-width="2"/>
    <circle cx="20" cy="20" r="9" fill="none" stroke="var(--blue)" stroke-width="2"/>
    <ellipse cx="20" cy="20" rx="4" ry="9" fill="none" stroke="var(--blue)" stroke-width="1.5"/>
    <line x1="11" y1="20" x2="29" y2="20" stroke="var(--blue)" stroke-width="1.5"/>
  </svg>
  <div class="abs center contact-big" style="top:330px">www.FieldlineNet.ca</div>

  <svg class="icon-circle" style="top:364px" viewBox="0 0 40 40">
    <circle cx="20" cy="20" r="18" fill="#fff" stroke="var(--blue)" stroke-width="2"/>
    <rect x="11" y="14" width="18" height="12" rx="1" fill="var(--blue)"/>
    <path d="M11 14 L20 21 L29 14" fill="none" stroke="#fff" stroke-width="1.4"/>
  </svg>
  <div class="abs center contact-big" style="top:408px">Sales@FieldlineNet.ca</div>

  <div class="abs center call">CALL US NOW</div>
  <div class="abs center phone">1 (833) 555-FIELD</div>
  <div class="abs center for-service">For Service</div>

  <p class="abs center proof">100% Canadian Owned &amp; Operated<br>Actual Results at a Rural Tower Site<small>(Available to all clients of that tower)</small></p>

  <div class="speed-result" role="img" aria-label="Speed test result screenshot: ping 9 ms, download 125.50 Mbps, upload 108.56 Mbps"></div>

  <svg class="blue-band" width="350" height="10" viewBox="0 0 350 10">
    <path d="M80 10 L92 4 H350 V10 Z" fill="var(--blue)"/>
  </svg>
</section>

</body>
</html>
```